Adoption Fundraising

We are in the midst of a fundraising campaign to raise the funds for our upcoming adoption of Mirek, a 9 year old orphan from Ukraine.
We would like it to include a picture of Mirek as well as one of the family pictures we had taken when he was here with us.

It should provide the addresses for our online fund raising site at www.GiveHarbor.example/ourtablewidens

It should also specify that more information on our adoption as well as how to make a tax deductible donation can be found on our website at www.OurTableWidens.example which should go live by tomorrow.

We are thinking that Ukrainian flag blue and yellow would be good colors to use but are open to other ideas.

Designers can also look at both of the above sites for additional info. and ideas.

It is also important to us to include the following scripture:

"Religion that God our Father accepts as pure and faultless is this: to look after orphans and widows in their distress..." James 1:27

We want this to be a two sided postcard that we can hand out personally and leave with area businesses and churches willing to make available to their customers/members.

Thanks so much!

Target Market(s)

The public in general age 18+

Industry/Entity Type

Flag

Requirements
Must have
• Must have the two web addresses and at least the picture of Mirek as well as the verse from James 1:27.
Nice to have
• Would also like to include one of the family photos. I'm envisioning using the family fence photo with the words, 'Our Table Widens' across the top of the card for the front and then Mirek's picture and all the other info on the back using the Ukrainian blue and yellow as the color scheme for the back.

```html
<!DOCTYPE html>
<html lang="en">
<head>
<meta charset="utf-8">
<title>Our Table Widens – Adoption Postcard</title>
<link rel="stylesheet" href="https://fonts.googleapis.com/css2?family=Londrina+Solid:wght@400;900&family=Amatic+SC:wght@700&family=Pacifico&family=Roboto+Condensed:wght@400;700&family=Kalam:wght@400&display=swap">
<style>
  :root{
    --forest-dark:#1f2e16;
    --forest-mid:#4d5f35;
    --meadow:#a9a36e;
    --cream:#fbf4d6;
    --title-cream:#f7eedd;
    --pink:#e5407c;
    --pink-bold:#d92f6e;
    --purple:#6a2a86;
    --gold-light:#e7d6a4;
    --gold-dark:#b89a5a;
    --ink:#3a2c14;
    --blue:#1c6fb8;
    --flag-blue:#2f6fd0;
    --flag-yellow:#f5d235;
    --white:#ffffff;
  }
  *{box-sizing:border-box;margin:0;padding:0}
  html,body{width:1200px;height:930px;overflow:hidden;background:var(--cream)}
  .postcard{position:relative;width:1200px;height:930px;overflow:hidden}
  .backdrop-photo{
    position:absolute;inset:0;
    background:linear-gradient(180deg,var(--forest-dark) 0%,#2f4222 30%,var(--forest-mid) 50%,var(--meadow) 62%,#d8cfa2 68%,var(--cream) 74%,var(--cream) 100%);
  }
  .family-group{
    position:absolute;left:70px;top:285px;width:1075px;height:380px;
    border-radius:120px 120px 40px 40px;
    background:
      linear-gradient(90deg,rgba(226,120,110,.55) 0%,rgba(235,200,180,.5) 18%,rgba(60,70,110,.55) 38%,rgba(230,110,130,.5) 48%,rgba(90,90,100,.5) 58%,rgba(220,120,130,.5) 75%,rgba(240,225,200,.5) 88%,rgba(225,130,140,.5) 100%);
    filter:blur(6px);
  }
  .title-small{
    position:absolute;left:338px;top:18px;
    font-family:"Londrina Solid",sans-serif;font-weight:400;
    font-size:54px;color:var(--title-cream);transform:rotate(-3deg);letter-spacing:1px;
  }
  .title-main{
    position:absolute;left:40px;top:70px;
    font-family:"Londrina Solid",sans-serif;font-weight:900;
    font-size:190px;line-height:1;color:var(--title-cream);
    letter-spacing:16px;transform:rotate(-5deg);
  }
  .site-ribbon{position:absolute;left:238px;top:226px;width:466px;height:66px;transform:rotate(-3deg)}
  .site-ribbon svg{position:absolute;inset:0}
  .site-ribbon span{
    position:absolute;inset:0;display:flex;align-items:center;justify-content:center;
    font-family:"Amatic SC",sans-serif;font-weight:700;font-size:34px;color:var(--forest-mid);
  }
  .verse-sticker{position:absolute;left:915px;top:-4px;width:250px;height:270px}
  .verse-sticker svg{position:absolute;inset:0}
  .verse-text{
    position:absolute;left:34px;top:44px;width:186px;
    font-family:"Kalam",cursive;font-size:16px;line-height:1.32;color:var(--ink);
    text-align:center;transform:rotate(-8deg);
  }
  .verse-text .ref{display:block;text-align:right;padding-right:14px}
  .story-heading{
    position:absolute;left:26px;top:540px;
    font-family:"Pacifico",cursive;font-weight:400;font-size:76px;line-height:1.3;color:var(--white);
    transform:rotate(-5deg);text-shadow:3px 3px 6px rgba(0,0,0,.35);
  }
  .story-body{
    position:absolute;left:6px;top:655px;width:922px;
    font-family:"Roboto Condensed",sans-serif;font-size:17px;line-height:26.5px;color:var(--pink);
  }
  .story-body strong{color:var(--pink-bold);font-weight:700}
  .story-body .fund-url{font-family:"Amatic SC",sans-serif;font-weight:700;font-size:28px;color:var(--purple);padding:0 6px}
  .child-polaroid{
    position:absolute;left:934px;top:482px;width:232px;height:262px;
    background:var(--white);padding:12px 12px 0;transform:rotate(4deg);
    box-shadow:0 3px 10px rgba(0,0,0,.35);
  }
  .child-photo{width:208px;height:188px;background:linear-gradient(160deg,#cfe3ea,#8fb8c4 60%,#d9b79a)}
  .child-name{
    display:block;text-align:center;margin-top:4px;
    font-family:"Pacifico",cursive;font-size:38px;line-height:52px;color:var(--blue);
  }
  .social-list{
    position:absolute;left:932px;top:770px;width:236px;
    display:grid;grid-template-columns:1fr 1fr;gap:18px 8px;list-style:none;
    font-family:"Roboto Condensed",sans-serif;font-weight:700;font-size:15px;color:var(--pink-bold);
  }
  .social-list li{display:flex;align-items:center;gap:6px;height:30px}
  .social-list .dot{width:14px;height:14px;border-radius:50%;background:var(--pink-bold)}
  .flag-mark{width:44px;height:30px;border-radius:4px;background:linear-gradient(180deg,var(--flag-blue) 50%,var(--flag-yellow) 50%)}
</style>
</head>
<body>
<main class="postcard">
  <div class="backdrop-photo" role="img" aria-label="Photo background: green trees above a sunlit meadow"></div>
  <div class="family-group" role="img" aria-label="Family photo: parents and ten children sitting and standing along a wooden fence"></div>

  <div class="title-small">Our Table</div>
  <h1 class="title-main">WIDENS</h1>

  <div class="site-ribbon">
    <svg viewBox="0 0 466 66" aria-hidden="true">
      <polygon points="0,8 466,0 452,33 466,62 0,66 14,37" fill="var(--title-cream)"/>
    </svg>
    <span>www.OurTableWidens.example</span>
  </div>

  <aside class="verse-sticker">
    <svg viewBox="0 0 250 270" aria-hidden="true">
      <defs>
        <radialGradient id="gold" cx="40%" cy="40%" r="65%">
          <stop offset="0" stop-color="var(--gold-light)"/>
          <stop offset="1" stop-color="var(--gold-dark)"/>
        </radialGradient>
      </defs>
      <circle cx="125" cy="135" r="120" fill="url(#gold)"/>
      <path d="M196 22 Q234 44 246 92 Q220 62 196 22Z" fill="#7a6434"/>
    </svg>
    <p class="verse-text">"Religion that God our Father accepts as pure and faultless is this: to look after orphans and widows in their distress..."<span class="ref">James 1:27</span></p>
  </aside>

  <h2 class="story-heading">The Story</h2>

  <section class="story-body">
    <p>In 2011 we hosted two Ukrainian orphans and the following year we followed God's calling on our lives to grow our 'already big family' through adoption! We stand amazed at what God is accomplishing through us and in these boys! They are not the same broken, hopeless children that we brought home and we praise God for that! This summer we stepped out in faith again with the hosting of another orphan; 9 year old Mirek. Once again God has placed adoption on our hearts.</p>
    <p>We would also be ever grateful for any financial assistance you could provide. Unfortunately the speed at which we are able to complete our adoption, as is the case with many adoptions, will depend in large part on how quickly the funds can be raised. Regardless of the amount, please do not underestimate the power of your gift. <strong>Every dollar counts!</strong></p>
    <p><strong>Thank you and God bless! Kindly visit</strong><span class="fund-url">www.GiveHarbor.example/ourtablewidens</span><strong>to make an easy,</strong></p>
    <p><strong>Tax-deductable donation.</strong></p>
  </section>

  <figure class="child-polaroid">
    <div class="child-photo" role="img" aria-label="Portrait photo of Mirek smiling"></div>
    <figcaption class="child-name">Mirek</figcaption>
  </figure>

  <ul class="social-list">
    <li><span class="dot"></span>Chirpline</li>
    <li><span class="dot"></span>Friendhall</li>
    <li><span class="dot"></span>Clipwall</li>
    <li><span class="dot"></span>Circleworks</li>
    <li><span class="dot"></span>Streamly</li>
    <li><span class="flag-mark" role="img" aria-label="Ukrainian flag colours"></span></li>
  </ul>
</main>
</body>
</html>
```